Business Card for Start Up Real Estate Company

We need a business card designed for a new real estate company called Belvanta. We plan on improving the experience of real estate transactions for both consumers and agents by using current and evolving technology. We would like to see designs that use our existing logo (attached). Please use a primarily white or light colored background. The final design should communicate technology, sophistication and customer service. Thank you...

Industry/Entity Type

Real Estate

Requirements
Must have
• Primarily white or light colored background
Nice to have
• Isolated A from our logo used as part of the design
Should not have
• Pictures, especially of houses

```html
<!DOCTYPE html>
<html lang="en">
<head>
<meta charset="utf-8">
<title>Belvanta Business Card</title>
<link href="https://fonts.googleapis.com/css2?family=Open+Sans:wght@400;600;700&display=swap" rel="stylesheet">
<style>
  :root {
    --brand-blue: #0e4f86;
    --brand-red: #d8192f;
    --paper: #f7f7f5;
    --ink-grey: #4a4a4a;
    --stage: #e4e5e7;
  }
  * { margin: 0; padding: 0; box-sizing: border-box; }
  html, body { width: 1200px; height: 800px; overflow: hidden; }
  body {
    background: var(--stage);
    font-family: "Open Sans", sans-serif;
    position: relative;
  }
  .card {
    position: absolute;
    top: 245px;
    width: 540px;
    height: 309px;
    overflow: hidden;
    box-shadow: 0 6px 18px rgba(0,0,0,0.15);
  }
  .card-back { left: 40px; background: var(--brand-blue); }
  .card-front { left: 620px; background: var(--paper); }

  .wordmark {
    position: absolute;
    font-family: "Open Sans", sans-serif;
    font-weight: 400;
    letter-spacing: 2px;
    text-transform: uppercase;
  }
  .card-back .wordmark {
    color: #ffffff;
    font-size: 56px;
    left: 0; right: 0; top: 112px;
    text-align: center;
  }
  .card-front .wordmark {
    color: var(--brand-blue);
    font-size: 40px;
    left: 34px; top: 92px;
  }

  .corner-tab {
    position: absolute;
    right: 0; top: 16px;
    width: 14px; height: 34px;
    background: var(--brand-red);
    border-radius: 6px 0 0 6px;
  }
  .holder {
    position: absolute;
    right: 34px; top: 24px;
    text-align: right;
  }
  .holder-name { color: var(--brand-blue); font-weight: 700; font-size: 17px; line-height: 1.2; }
  .holder-role { color: var(--ink-grey); font-size: 11px; }

  .address {
    position: absolute;
    right: 34px; top: 120px;
    text-align: right;
    color: var(--ink-grey);
    font-size: 12px;
    line-height: 1.4;
  }

  .contacts {
    position: absolute;
    left: 34px; bottom: 40px;
    list-style: none;
    color: var(--ink-grey);
    font-size: 12px;
    line-height: 1.5;
  }
  .contacts li { display: flex; align-items: center; gap: 8px; }
  .contacts svg { width: 12px; height: 12px; fill: var(--brand-red); }

  .edge-stripes { position: absolute; left: 0; right: 0; bottom: 0; }
  .edge-stripes .red-line { height: 4px; background: var(--brand-red); }
  .edge-stripes .gap { height: 3px; background: var(--paper); }
  .edge-stripes .blue-band { height: 12px; background: var(--brand-blue); }
</style>
</head>
<body>
  <section class="card card-back" aria-label="Card back">
    <div class="wordmark">Belvanta</div>
  </section>

  <section class="card card-front" aria-label="Card front">
    <div class="corner-tab"></div>
    <div class="holder">
      <div class="holder-name">Marcus Ellery</div>
      <div class="holder-role">President / Owner</div>
    </div>

    <div class="wordmark">Belvanta</div>

    <address class="address" style="font-style:normal">
      Harbor Lane Address,<br>Brookfield 40218
    </address>

    <ul class="contacts">
      <li>
        <svg viewBox="0 0 24 24" aria-hidden="true"><path d="M6.6 10.8a15 15 0 0 0 6.6 6.6l2.2-2.2c.3-.3.7-.4 1-.2 1.1.4 2.3.6 3.6.6.6 0 1 .4 1 1V20c0 .6-.4 1-1 1C10.6 21 3 13.4 3 4c0-.6.4-1 1-1h3.5c.6 0 1 .4 1 1 0 1.3.2 2.5.6 3.6.1.3 0 .7-.2 1z"/></svg>
        +1 312 555 0147
      </li>
      <li>
        <svg viewBox="0 0 24 24" aria-hidden="true"><path d="M7 2h10a2 2 0 0 1 2 2v16a2 2 0 0 1-2 2H7a2 2 0 0 1-2-2V4a2 2 0 0 1 2-2zm0 3v13h10V5zm5 14.2a1 1 0 1 0 0 .1z"/></svg>
        +1 312 555 0148
      </li>
      <li>
        <svg viewBox="0 0 24 24" aria-hidden="true"><path d="M7 2h10a2 2 0 0 1 2 2v16a2 2 0 0 1-2 2H7a2 2 0 0 1-2-2V4a2 2 0 0 1 2-2zm0 3v13h10V5z"/></svg>
        +1 312 555 0193
      </li>
      <li>
        <svg viewBox="0 0 24 24" aria-hidden="true"><path d="M2 5h20v14H2zm2 2v.5l8 5 8-5V7zm0 2.8V17h16V9.8l-8 5z"/></svg>
        mellery@belvanta.com
      </li>
      <li>
        <svg viewBox="0 0 24 24" aria-hidden="true"><path d="M12 2a10 10 0 1 0 0 20 10 10 0 0 0 0-20zm6.9 9h-3a15 15 0 0 0-1.3-5.9A8 8 0 0 1 18.9 11zM12 4c.9 1.2 1.8 3.6 1.9 7h-3.8c.1-3.4 1-5.8 1.9-7zM9.4 5.1A15 15 0 0 0 8.1 11h-3a8 8 0 0 1 4.3-5.9zM5.1 13h3a15 15 0 0 0 1.3 5.9A8 8 0 0 1 5.1 13zM12 20c-.9-1.2-1.8-3.6-1.9-7h3.8c-.1 3.4-1 5.8-1.9 7zm2.6-1.1a15 15 0 0 0 1.3-5.9h3a8 8 0 0 1-4.3 5.9z"/></svg>
        www.belvanta.com
      </li>
    </ul>

    <div class="edge-stripes">
      <div class="red-line"></div>
      <div class="gap"></div>
      <div class="blue-band"></div>
    </div>
  </section>
</body>
</html>
```